BRVO Membership Certificate

We are launching an online membership for www.brvo.com

When someone joins they will receive a membership certificate that outlines their name, membership number, membership status, date of membership

```html
<!DOCTYPE html>
<html lang="en">
<head>
<meta charset="utf-8">
<title>BRVO Membership Certificate</title>
<link rel="stylesheet" href="https://fonts.googleapis.com/css2?family=Barlow+Semi+Condensed:wght@500&family=Playfair+Display:ital,wght@1,500&family=Poppins:ital,wght@0,400;0,500;0,700;0,800;1,400;1,700&display=swap">
<style>
  :root {
    --yellow: #e8c61c;
    --blue: #214a8c;
    --navy: #233a6e;
    --ink: #0d1633;
    --charcoal: #231f20;
    --paper: #ffffff;
  }
  * { margin: 0; padding: 0; box-sizing: border-box; }
  html, body { width: 1200px; height: 849px; overflow: hidden; background: var(--blue); }
  .certificate {
    position: relative;
    width: 1200px; height: 849px;
    background: linear-gradient(to bottom, var(--yellow) 0 462px, var(--blue) 462px 100%);
    font-family: "Poppins", sans-serif;
    color: var(--ink);
  }
  .certificate-frame {
    position: absolute;
    left: 63px; top: 63px; width: 1074px; height: 722px;
    background: var(--blue);
    border-radius: 22px;
  }
  .certificate-card {
    position: absolute;
    left: 70px; top: 70px; width: 1060px; height: 708px;
    background: var(--paper);
    border-radius: 16px;
  }
  .brand {
    position: absolute;
    left: 478px; top: 96px;
    display: flex; align-items: center; gap: 14px;
  }
  .brand-mark {
    width: 80px; height: 80px; border-radius: 50%;
    background: var(--blue);
  }
  .brand-name {
    font-family: "Barlow Semi Condensed", sans-serif;
    font-weight: 500;
    font-size: 22px;
    line-height: 23.5px;
    color: var(--blue);
    text-transform: uppercase;
  }
  .heading-art { position: absolute; left: 0; top: 0; }
  .title-arc { font-family: "Poppins", sans-serif; font-weight: 800; font-size: 74px; }
  .title-arc .shadow { fill: var(--yellow); }
  .title-arc .face { fill: var(--navy); }
  .ribbon { fill: var(--blue); }
  .ribbon-text {
    font-family: "Poppins", sans-serif; font-weight: 700;
    font-size: 21px; letter-spacing: 2.6px; fill: var(--paper);
  }
  .subtitle {
    position: absolute; left: 0; width: 1200px; top: 300px;
    text-align: center;
    font-size: 34px; font-weight: 400; letter-spacing: 0.5px;
    color: var(--charcoal);
  }
  .member-name {
    position: absolute; left: 0; width: 1200px; top: 405px;
    text-align: center;
    font-family: "Playfair Display", serif; font-style: italic; font-weight: 500;
    font-size: 68px; color: var(--ink);
  }
  .statement {
    position: absolute; left: 0; width: 1200px; top: 497px;
    text-align: center;
    font-size: 23px; font-style: italic; line-height: 36px;
    letter-spacing: 0.6px; color: var(--ink);
  }
  .statement strong { font-weight: 700; }
  .field {
    position: absolute; width: 267px; text-align: center;
    font-size: 19px; font-weight: 500; letter-spacing: 0.9px; color: var(--ink);
  }
  .field::before {
    content: ""; display: block; height: 0;
    border-top: 2px dotted var(--ink);
    margin-bottom: 8px;
  }
  .field-number { left: 152px; top: 625px; }
  .field-status { left: 466px; top: 625px; }
  .field-date { left: 782px; top: 625px; }
  .field-signature { left: 427px; top: 716px; width: 347px; }
</style>
</head>
<body>
<main class="certificate">
  <div class="certificate-frame"></div>
  <div class="certificate-card"></div>

  <div class="brand">
    <div class="brand-mark"></div>
    <div class="brand-name">Broadview<br>Relationship<br>Value<br>Organisation</div>
  </div>

  <svg class="heading-art" width="1200" height="849" viewBox="0 0 1200 849" aria-hidden="true">
    <defs>
      <path id="title-curve" d="M 315 322 A 978 978 0 0 1 885 322"/>
    </defs>
    <g class="title-arc">
      <text class="shadow" transform="translate(4 3)" text-anchor="middle">
        <textPath href="#title-curve" startOffset="50%" textLength="540" lengthAdjust="spacingAndGlyphs">CERTIFICATE</textPath>
      </text>
      <text class="face" text-anchor="middle">
        <textPath href="#title-curve" startOffset="50%" textLength="540" lengthAdjust="spacingAndGlyphs">CERTIFICATE</textPath>
      </text>
    </g>
    <polygon class="ribbon" points="402,357 797,357 782,375.5 797,394 402,394 417,375.5"/>
    <text class="ribbon-text" x="603" y="383.5" text-anchor="middle">THIS IS TO CERTIFY THAT</text>
  </svg>

  <div class="subtitle">OF MEMBERSHIP</div>

  <div class="member-name">Name Surname</div>

  <p class="statement">has successfully joined <strong>Broadview Relationship</strong><br><strong>Value Organisation (BRVO)</strong> as a valued member</p>

  <div class="field field-number">Membership Number</div>
  <div class="field field-status">Membership Status</div>
  <div class="field field-date">Date of Membership</div>
  <div class="field field-signature">Director’s Signature</div>
</main>
</body>
</html>
```